Corwith Lodge website redesign

After 8 years of our current site, we're ready to upgrade our site design. We'd like to generally make it more modern and clean and build it on a CMS like joomla for easier future maintenance.

Our hotel is a family-owned bed and breakfast that competes against much larger hotel chains in Aspen with fancier rooms and larger pricetags. Our hotel is priced moderately and features tasteful, uniquely-design rooms.

We are looking for a website that will showcase the uniqueness of our rooms, the history of the Lodge, and the friendliness of our staff.

Here are some other hotel sites we like:

http://www.brackenfoldhouse.example/

http://www.tollerpeakhaus.example/

http://www.quarrowstay.example/

*********

Scope of Work - I'm looking for a design AND build. The website should be built out in Joomla as part of the final deliverable.
Updates

Current website: http://www.corwithlodge.example/

Explanation of what design + build means:

I am looking for not only the design of the site, but also for the homepage and one subpage to be built out as well. I do NOT need the entire site built - only for those two pages to be built and I will retrofit the remainder of the pages.

Target Market(s)

travellers evaluating hotels in Aspen, Colorado.

Industry/Entity Type

Hotel

Requirements
Must have
• Must, must, must be based on a joomla template. "Rotating" large main image as central position on homepage is a must (see example websites mentioned above).

Nice to have
• We have an existing online reservation system. It would be nice to evaluate placing a "widget" on the homepage that integrates to the online reservation page. Similar to that feature that the Bracken Fold website has at the foot of the main image on their homepage.

```html
<!DOCTYPE html>
<html lang="en">
<head>
<meta charset="utf-8">
<title>Corwith Lodge – Rooms and Rates</title>
<link rel="stylesheet" href="https://fonts.googleapis.com/css2?family=PT+Sans:wght@400;700&family=Playball&display=swap">
<style>
:root{
  --red:#9c1c1c;
  --red-dark:#7a1010;
  --cream:#fbe6c6;
  --panel:#fdf3e1;
  --band:#f9dcb4;
  --text:#2b1d12;
  --accent:#a3341a;
  --gold:#f2d54a;
  --btn:#e8a35a;
  --rule:#d9c1a0;
}
*{margin:0;padding:0;box-sizing:border-box}
html,body{width:903px;height:1200px;overflow:hidden}
body{font-family:"PT Sans",sans-serif;color:var(--text);background:var(--cream);position:relative;font-size:9.5px}
.abs{position:absolute}
.header{left:0;top:0;width:903px;height:58px;background:#fff}
.logo{left:120px;top:12px;font-size:28px;color:#1a1a1a;font-weight:400}
.contacts{right:120px;top:21px;display:flex;align-items:center;gap:18px;font-size:11px;white-space:nowrap}
.contact{display:flex;align-items:center;gap:6px}
.nav{left:0;top:58px;width:903px;height:26px;background:linear-gradient(var(--red),var(--red-dark));display:flex;justify-content:center;align-items:center;gap:8px;color:#fff;font-size:10px}
.nav span.sep{opacity:.8}
.nav .on{color:var(--gold)}
.hero{left:0;top:84px;width:903px;height:207px;background:linear-gradient(90deg,#4a3323,#8a6040 35%,#c48c52 60%,#5a3d28)}
.sidenav{left:119px;top:300px;width:165px;list-style:none}
.sidenav li{height:23px;line-height:18px;border-bottom:1px solid #ead1ad;padding-left:10px;position:relative;font-size:9px}
.sidenav li::before{content:"";position:absolute;left:0;top:5px;border-left:5px solid var(--red);border-top:3px solid transparent;border-bottom:3px solid transparent}
.sidenav li.on{color:var(--accent)}
.script{font-family:"Playball",cursive;color:var(--accent)}
.ratebox{left:120px;top:452px;width:165px;height:126px;background:#fff8ee;border:1px solid #ecd5b4;border-radius:5px;box-shadow:0 0 4px #e6c9a2}
.row{position:absolute;left:0;font-size:8.5px;text-align:right}
.field{position:absolute;left:57px;height:17px;border:1px solid #ddd;background:#fff}
.submit{left:104px;top:92px;width:45px;height:18px;background:linear-gradient(#f0a93a,#c57410);color:#fff;font-weight:700;font-size:8.5px;text-align:center;line-height:18px;border-radius:2px}
.main{left:303px;top:341px;width:480px;height:755px;background:var(--panel);border-bottom:6px solid var(--band)}
.band{height:35px;background:var(--band);color:var(--accent);font-size:12px;line-height:35px;padding-left:14px}
.room{position:absolute;left:15px;width:450px}
.photo{position:absolute;left:0;top:0;width:203px;height:149px;border:3px solid #fff;box-shadow:0 0 2px #bba}
.book{position:absolute;left:0;top:157px;width:73px;height:20px;background:linear-gradient(#f5c07a,var(--btn));border-radius:4px;color:#fff;font-size:8px;text-align:center;line-height:20px}
.info{position:absolute;left:215px;top:0;width:225px}
.info h3{color:var(--accent);font-weight:400;font-size:11px;margin-bottom:3px}
.info ul{list-style:none}
.info li{font-size:9px;line-height:16.5px;padding-left:9px;position:relative}
.info li::before{content:"";position:absolute;left:0;top:5px;border-left:5px solid var(--red);border-top:3px solid transparent;border-bottom:3px solid transparent}
.info h4{color:var(--accent);font-size:8.5px;margin-top:10px}
.info p{font-size:8px;line-height:14.5px}
.divider{position:absolute;left:15px;width:450px;border-top:1px solid var(--rule)}
.names{left:15px;top:708px;font-size:8px;line-height:14px}
.names a{color:var(--accent);text-decoration:underline}
.footer{left:0;top:1120px;width:903px;height:80px;background:#fff;border-top:1px solid #eedbbf}
.flinks{right:120px;top:24px;text-align:right;font-size:8px;line-height:13px}
.copy{color:#666;font-size:7px}
</style>
</head>
<body>
<header class="abs header">
  <div class="abs logo">Corwith Lodge</div>
  <div class="abs contacts">
    <div class="contact">
      <svg width="16" height="11" viewBox="0 0 16 11"><rect width="16" height="11" fill="#f2c23a"/><path d="M0 0L8 6L16 0" fill="none" stroke="#c9911a"/></svg>
      <span>info@corwithlodge.example</span>
    </div>
    <div class="contact">
      <svg width="14" height="11" viewBox="0 0 14 11"><path d="M1 4Q7-1 13 4L11 5L10 3Q7 2 4 3L3 5Z" fill="#111"/><rect x="3" y="5" width="8" height="6" rx="1" fill="#111"/></svg>
      <span>Call 877 555 0142</span>
    </div>
  </div>
</header>
<nav class="abs nav">
  <span>ABOUT LODGE</span><span class="sep">|</span><span class="on">ROOMS</span><span class="sep">|</span><span>RESERVATIONS</span><span class="sep">|</span><span>AMENITIES</span><span class="sep">|</span><span>ASPEN INFORMATION</span><span class="sep">|</span><span>MANGER'S JOURNAL</span><span class="sep">|</span><span>WEBCAMS</span><span class="sep">|</span><span>CONTACT US</span>
</nav>
<div class="abs hero" role="img" aria-label="Photo of the lodge's evening patio lounge with sofas and a fireplace"></div>

<ul class="abs sidenav">
  <li>Overview</li><li class="on">Premium Rooms</li><li>Deluxe Rooms</li><li>Standard Rooms</li><li>Hotel Photo Gallery</li>
</ul>
<div class="abs script" style="left:119px;top:422px;font-size:17px">Rates &amp; Availability</div>
<div class="abs ratebox">
  <div class="row" style="top:20px;width:55px">Arrival :</div><div class="field" style="top:16px;width:92px"></div>
  <div class="row" style="top:45px;width:55px">Departure :</div><div class="field" style="top:41px;width:92px"></div>
  <div class="row" style="top:70px;width:55px">Adults :</div><div class="field" style="top:66px;width:39px"></div>
  <div class="row" style="top:96px;width:55px">Children :</div><div class="field" style="top:92px;width:39px"></div>
  <div class="abs submit">SUBMIT</div>
</div>

<div class="abs script" style="left:303px;top:300px;font-size:22px">Rooms and Rates</div>
<div class="abs" style="left:303px;top:331px;width:480px;border-top:1px solid var(--rule)"></div>

<main class="abs main">
  <div class="band">PREMIUM ROOMS</div>
  <section class="room" style="top:52px">
    <div class="photo" role="img" aria-label="Spruce room with queen bed and iron headboard" style="background:linear-gradient(135deg,#b99a66,#e3d5b0 60%,#6d5a3c)"></div>
    <div class="book">Book This Room</div>
    <div class="info">
      <h3>Spruce</h3>
      <ul><li>One Queen Bed</li><li>Mountain View</li><li>Balcony</li><li>Fireplace</li><li>Sleeps Two Adults</li></ul>
      <h4>All Rooms Include:</h4>
      <p>Flat Panel TV w/ Cable, High Speed Internet Access, Two Telephones with Speakerphone and Voicemail features, CD Player/AM-FM Clock Radio, &amp; Individually Controlled Heating/Cooling Systems</p>
    </div>
  </section>
  <div class="divider" style="top:252px"></div>
  <section class="room" style="top:275px">
    <div class="photo" role="img" aria-label="Elevator Shaft room with two full beds" style="background:linear-gradient(135deg,#d8c6a6,#8a6a48 55%,#4b3a2c)"></div>
    <div class="book">Book This Room</div>
    <div class="info">
      <h3>Elevator Shaft</h3>
      <ul><li>Two Full Beds</li><li>Mountain View</li><li>Sleeps Four Adults</li></ul>
      <h4>All Rooms Include:</h4>
      <p>Flat Panel TV w/ Cable, High Speed Internet Access, 2 Telephones, CD Player/AM-FM Clock Radio, &amp; Individually Controlled Heating/Cooling.</p>
    </div>
  </section>
  <div class="divider" style="top:475px"></div>
  <section class="room" style="top:499px">
    <div class="photo" role="img" aria-label="Tie Hack room with king four-poster bed" style="background:linear-gradient(135deg,#c9a56a,#7a3a2a 55%,#2e2218)"></div>
    <div class="book">Book This Room</div>
    <div class="info">
      <h3>Tie Hack</h3>
      <ul><li>One King Bed</li><li>Mountain View</li><li>Fireplace</li><li>Sleeps Two Adults</li></ul>
      <h4>All Rooms Include:</h4>
      <p>Flat Panel TV w/ Cable, High Speed Internet Access, 2 Telephones, CD Player/AM-FM Clock Radio, &amp; Individually Controlled Heating/Cooling.</p>
    </div>
  </section>
  <div class="abs names"><b>Room Names:</b><br><a>Spruce</a>, &nbsp;<a>Elevator Shaft</a>, &nbsp;<a>Tie Hack</a>, <a>Karen's</a>, <a>Cloud Nine</a>, <a>Midnight</a></div>
</main>

<footer class="abs footer">
  <svg class="abs" style="left:120px;top:16px" width="50" height="50" role="img" aria-label="Review badge"><circle cx="25" cy="25" r="24" fill="#8a9a5a"/></svg>
  <svg class="abs" style="left:181px;top:22px" width="34" height="34"><rect width="34" height="34" rx="4" fill="#e8eef5"/></svg>
  <div class="abs" style="left:223px;top:21px;font-size:8.5px;line-height:12px"><b style="color:#2b4a8a">We're on Socialpage</b><br>like us to see our daily updates!</div>
  <div class="abs" style="left:221px;top:46px;display:flex;gap:4px;font-size:7px">
    <span style="border:1px solid #bcc;padding:1px 4px;background:#eef">Like</span><span style="border:1px solid #ccc;padding:1px 3px">732</span><span style="border:1px solid #bcc;padding:1px 4px;background:#eef">Send</span>
  </div>
  <div class="abs flinks">About Lodge &nbsp;-&nbsp; Rooms &nbsp;-&nbsp; Reservations &nbsp;-&nbsp; Amenities &nbsp;-&nbsp; Aspen Information<br>- &nbsp;Manger's Journal &nbsp;-&nbsp; Webcams &nbsp;-&nbsp; Contact Us<br><span class="copy">©2012 &nbsp;www.corwithlodge.example All rights reserved</span></div>
</footer>
</body>
</html>
```